Skill Up Salary Up

Full Page
7.5 w x 10 h / 8 w x 10.75 h + .25" bleed
Full-Page Career Course Ad
Project Overview
• Goal: Create a visually attractive, modern, and uncluttered full-page magazine advertisement to list available career courses.
• Tone: Creative, professional, and attention-grabbing to prevent the reader from turning the page. The final design must prioritize readability.

Content Requirements
1. Header/Headline: Must be the primary focus. And grab peoples attention
2. Course Listing: A clear, well-organized list of the career courses.
________________________________________
Design & Aesthetic Directives
1. Layout & Readability (Crucial)
• The final ad must not look crowded or busy.
• Prioritize white space to make the text "breathe" and ensure the course list is easy to scan and read.
• Use a modern, clean, and professional typeface (font choice is critical for the aesthetic).
2. Visual Style
• Aim for a creative, modern, and fresh look. Avoid outdated or generic stock imagery/layouts.
3. Imagery/Graphic Element (Artist's Choice)
You have creative freedom regarding the main graphic element.
• Option A (Photography): Use a photo of a white male American with a collared shirt. The imagery should convey success, focus, or professional development.
• Option B (Vector/Illustration): Use a modern vector graphic, illustration, or abstract design. This could be used to symbolize growth, connection, or a career path.
The choice of graphic element is yours, but it must support the overall modern and uncrowded aesthetic.

Requirements
Must have
• Partial listing .. is part of the Harbor Lantern Course

```html
<!DOCTYPE html>
<html lang="en">
<head>
<meta charset="utf-8">
<title>Skill Up Salary Up – Upcoming ARQ Courses</title>
<link rel="stylesheet" href="https://fonts.googleapis.com/css2?family=Anton&family=Archivo+Black&family=Montserrat:wght@800;900&family=Oswald:wght@500;600&family=Poppins:wght@400;500;600&display=swap">
<style>
  :root {
    --blue: #2196d1;
    --blue-soft: #e7f1f7;
    --ink: #333335;
    --dark-disc: #3a3a3c;
    --backdrop: #d6d6d6;
    --paper: #ffffff;
  }
  * { margin: 0; padding: 0; box-sizing: border-box; }
  html, body { width: 891px; height: 1200px; overflow: hidden; background: var(--backdrop); }
  body { font-family: "Poppins", sans-serif; color: var(--ink); }

  .ad-page {
    position: absolute; left: 92px; top: 81px; width: 692px; height: 1038px;
    background: var(--paper); overflow: hidden;
  }
  .abs { position: absolute; }
  .line { position: absolute; transform: translateY(-50%); white-space: nowrap; }

  .backdrop-shapes { position: absolute; inset: 0; }
  .hero-photo {
    position: absolute; left: 410px; top: 43px; width: 282px; height: 499px;
    background: linear-gradient(180deg, #e9edf0 0%, #f4f6f8 60%, rgba(231,241,247,0.9) 100%);
    border-radius: 130px 130px 0 0;
  }

  .headline-skill { left: 27px; top: 22px; font: 900 67px/1 "Montserrat", sans-serif; color: var(--blue); letter-spacing: -1px; }
  .headline-salary { left: 27px; top: 80px; font: 800 50px/1 "Montserrat", sans-serif; color: var(--ink); letter-spacing: -1px; }
  .headline-upcoming { left: 27px; top: 147px; font: 400 40px/1 "Archivo Black", sans-serif; color: var(--blue); letter-spacing: 1px; transform: scaleX(1.22); transform-origin: left; }
  .headline-courses { left: 25px; top: 186px; font: 400 66px/1 "Anton", sans-serif; color: var(--ink); letter-spacing: -0.5px; }
  .tagline { left: 29px; top: 263px; font: 600 14px/1 "Oswald", sans-serif; color: var(--blue); letter-spacing: -0.2px; }

  .band { position: absolute; }
  .band-title { position: absolute; transform: translateY(-50%); font: 500 21px/1 "Oswald", sans-serif; color: #fff; white-space: nowrap; }

  .lead { font-weight: 600; font-size: 14px; }
  .lead-sm { font-weight: 600; font-size: 13px; }
  .body { font-size: 13px; }
  .kicker { font-weight: 500; font-size: 14px; color: var(--blue); }
  .section-label { font-weight: 500; font-size: 15px; }

  .dot-bullet { padding-left: 16px; }
  .dot-bullet::before {
    content: ""; position: absolute; left: 0; top: 50%; width: 9px; height: 9px; margin-top: -5px;
    border: 1.3px solid var(--blue); border-radius: 50%;
    background: radial-gradient(circle, var(--blue) 0 2px, transparent 2.4px);
  }
  .dot-bullet.small { padding-left: 13px; }
  .dot-bullet.small::before { width: 7px; height: 7px; margin-top: -4px; background: radial-gradient(circle, var(--blue) 0 1.5px, transparent 1.8px); }
  .diamond-bullet { padding-left: 10px; }
  .diamond-bullet::before {
    content: ""; position: absolute; left: 0; top: 50%; width: 5px; height: 5px; margin-top: -3px;
    border: 1.3px solid var(--blue); transform: rotate(45deg); background: radial-gradient(circle, var(--blue) 0 1px, transparent 1.3px);
  }

  .badge {
    position: absolute; width: 79px; height: 79px; border-radius: 50%;
    display: flex; align-items: center; justify-content: center; text-align: center;
    font: 600 12.5px/1.25 "Poppins", sans-serif; color: #fff;
  }
  .badge-blue { background: var(--blue); box-shadow: 4px 4px 10px rgba(33,150,209,0.25); }
  .badge-dark { background: var(--dark-disc); }
</style>
</head>
<body>
<main class="ad-page">
  <svg class="backdrop-shapes" viewBox="0 0 692 1038" width="692" height="1038" aria-hidden="true">
    <polygon points="473,581 604,581 692,700 692,1038 340,1038" fill="var(--blue-soft)"/>
    <polygon points="532,0 692,170 692,180 632,177 632,320 470,320 470,172 364,167" fill="var(--blue)"/>
  </svg>

  <div class="hero-photo" role="img" aria-label="Smiling young man in a white collared shirt giving a thumbs up"></div>

  <h1>
    <span class="abs headline-skill">SKILL UP</span>
    <span class="abs headline-salary">SALARY UP</span>
    <span class="abs headline-upcoming">UPCOMING</span>
    <span class="abs headline-courses">ARQ COURSES</span>
  </h1>
  <p class="abs tagline">MEN &amp; WOMEN • IN-PERSON &amp; REMOTE • PARTIAL SCHOLORASHIPS</p>

  <!-- Harbor Lantern Course -->
  <section class="course course-harbor">
    <svg class="band" style="left:0;top:295px" width="248" height="36" viewBox="0 0 248 36" aria-hidden="true">
      <polygon points="0,0 245,0 230,34 0,34" fill="var(--blue)"/>
      <line x1="0" y1="35.5" x2="230" y2="35.5" stroke="var(--blue)" stroke-width="1"/>
      <line x1="236" y1="2" x2="224" y2="32" stroke="#fff" stroke-width="2"/>
    </svg>
    <h2 class="band-title" style="left:29px;top:312px">Harbor Lantern Course</h2>
    <p class="line lead" style="left:29px;top:346px">Business Skills &amp; Knowledge to:</p>
    <p class="line body dot-bullet" style="left:29px;top:372px">Impress your interviewer</p>
    <p class="line body dot-bullet" style="left:29px;top:392px">Maximize Income</p>
    <p class="line body dot-bullet" style="left:29px;top:413px">Start / Run Your Business</p>
    <p class="line section-label" style="left:30px;top:443px">PARTIAL LISTING</p>
    <p class="line body diamond-bullet" style="left:30px;top:469px">Computers</p>
    <p class="line body diamond-bullet" style="left:30px;top:488px">Marketing</p>
    <p class="line body diamond-bullet" style="left:30px;top:508px">Sales</p>
    <p class="line body diamond-bullet" style="left:30px;top:527px">Finance</p>
    <p class="line body diamond-bullet" style="left:129px;top:469px">Healthcare</p>
    <p class="line body diamond-bullet" style="left:129px;top:488px">Business Strategy</p>
    <p class="line body diamond-bullet" style="left:129px;top:508px">Communication</p>
    <p class="line body diamond-bullet" style="left:129px;top:527px">LedgerBooks</p>
    <p class="line body diamond-bullet" style="left:271px;top:469px">Investments</p>
    <p class="line body diamond-bullet" style="left:271px;top:488px">Real Estate</p>
    <p class="line body diamond-bullet" style="left:271px;top:508px">Accounting</p>
    <div class="badge badge-blue" style="left:234px;top:375px">4-5<br>MONTHS<br>NOV 2025</div>
  </section>

  <!-- Software, Web & Apps -->
  <section class="course course-software">
    <svg class="band" style="left:0;top:547px" width="245" height="38" viewBox="0 0 245 38" aria-hidden="true">
      <polygon points="0,0 243,0 228,35 0,35" fill="var(--blue)"/>
      <line x1="0" y1="37" x2="228" y2="37" stroke="var(--blue)" stroke-width="1"/>
      <line x1="234" y1="2" x2="222" y2="33" stroke="#fff" stroke-width="2"/>
    </svg>
    <h2 class="band-title" style="left:24px;top:565px">Software, Web &amp; Apps</h2>
    <p class="line lead-sm" style="left:30px;top:601px"># 2 Best Tech Job</p>
    <p class="line lead-sm" style="left:28px;top:617px">National Career Review 2025</p>
    <p class="line kicker" style="left:26px;top:642px">JOB OPPORTUNITIES</p>
    <p class="line body dot-bullet small" style="left:26px;top:668px">Computer Programmer</p>
    <p class="line body dot-bullet small" style="left:26px;top:686px">Software Developer/Mobile</p>
    <p class="line body dot-bullet small" style="left:26px;top:703px">Engineer Developer (Apps</p>
    <p class="line lead-sm" style="left:30px;top:733px">Optional:</p>
    <p class="line body" style="left:30px;top:748px">Bachelors in Prog. &amp;Tech</p>
    <div class="badge badge-dark" style="left:234px;top:587px">NOV<br>2025</div>
  </section>

  <!-- IT Desktop & Networking Support -->
  <section class="course course-it">
    <svg class="band" style="left:358px;top:543px" width="334" height="40" viewBox="0 0 334 40" aria-hidden="true">
      <polygon points="18,3 334,3 334,38 4,38" fill="var(--blue)"/>
      <line x1="16" y1="0.5" x2="334" y2="0.5" stroke="var(--blue)" stroke-width="1"/>
      <line x1="12" y1="5" x2="0" y2="37" stroke="var(--blue)" stroke-width="1"/>
      <line x1="26" y1="5" x2="14" y2="37" stroke="#fff" stroke-width="2"/>
    </svg>
    <h2 class="band-title" style="left:408px;top:563px">IT Desktop &amp; Networking Support</h2>
    <p class="line lead-sm" style="left:410px;top:597px">#2 Best Job</p>
    <p class="line lead-sm" style="left:408px;top:613px">National Career Review 2025</p>
    <p class="line kicker" style="left:408px;top:642px">MASTERS IT</p>
    <p class="line body dot-bullet small" style="left:410px;top:668px">Desktop OS</p>
    <p class="line body dot-bullet small" style="left:410px;top:686px">Networks</p>
    <p class="line body dot-bullet small" style="left:410px;top:703px">Servers</p>
    <p class="line body dot-bullet small" style="left:410px;top:721px">Cloud</p>
    <div class="badge badge-blue" style="left:536px;top:640px">7<br>MONTHS<br>DEC 2025</div>
  </section>

  <!-- Brightdesk Office - Computers -->
  <section class="course course-office">
    <svg class="band" style="left:360px;top:750px" width="332" height="40" viewBox="0 0 332 40" aria-hidden="true">
      <polygon points="18,3 332,3 332,38 4,38" fill="var(--blue)"/>
      <line x1="16" y1="0.5" x2="332" y2="0.5" stroke="var(--blue)" stroke-width="1"/>
      <line x1="12" y1="5" x2="0" y2="37" stroke="var(--blue)" stroke-width="1"/>
      <line x1="26" y1="5" x2="14" y2="37" stroke="#fff" stroke-width="2"/>
    </svg>
    <h2 class="band-title" style="left:407px;top:770px">Brightdesk Office- Computers</h2>
    <p class="line lead-sm" style="left:410px;top:805px">The New&nbsp;&nbsp; Job Prerequisite</p>
    <p class="line body dot-bullet small" style="left:414px;top:835px">Sheets</p>
    <p class="line body dot-bullet small" style="left:414px;top:853px">Docs</p>
    <p class="line body dot-bullet small" style="left:414px;top:870px">Email</p>
    <p class="line body dot-bullet small" style="left:414px;top:888px">Slides</p>
    <p class="line body" style="left:419px;top:919px">Computer lab available to practice</p>
    <div class="badge badge-dark" style="left:538px;top:818px">5<br>WEEKS<br>DEC 2025</div>
  </section>

  <!-- Bookkeeping LedgerBooks -->
  <section class="course course-bookkeeping">
    <svg class="band" style="left:0;top:782px" width="256" height="38" viewBox="0 0 256 38" aria-hidden="true">
      <polygon points="0,0 254,0 239,36 0,36" fill="var(--blue)"/>
      <line x1="0" y1="37.5" x2="239" y2="37.5" stroke="var(--blue)" stroke-width="1"/>
      <line x1="246" y1="2" x2="234" y2="34" stroke="#fff" stroke-width="2"/>
    </svg>
    <h2 class="band-title" style="left:29px;top:800px">Bookkeeping LedgerBooks</h2>
    <p class="line lead-sm" style="left:28px;top:838px">Train for a quality job</p>
    <p class="line lead-sm" style="left:28px;top:854px">Manage your own books</p>
    <p class="line kicker" style="left:26px;top:879px">JOB OPPORTUNITIES</p>
    <p class="line body dot-bullet small" style="left:26px;top:902px">Finance Management</p>
    <p class="line body dot-bullet small" style="left:26px;top:920px">Customer &amp; Vendor Mgmt.</p>
    <p class="line body dot-bullet small" style="left:26px;top:937px">Advanced Tools</p>
    <div class="badge badge-blue" style="left:235px;top:839px">5<br>WEEKS<br>NOV 2025</div>
  </section>
</main>
</body>
</html>
```